Recreating a Opt-in for a FREE BOOK for brides.

I need to have an opt-in box recreated to make brides want to get my free book. The opt-in message is already on the mock website. It needs to look graphically pleasing in the colors being used, but bold enough to grab the viewers attention. I am including the link to the website where the graphic needs to be re-created. You'll notice there are two areas where the graphics need to go.

Target Market(s)

Brides

Requirements
Must have
• Begin by looking at the website..http://qvotrl.com/zu-pim/
On the homepage is the current "A Gift For You" graphic. (I have included an image of the home page for the circled area that needs to be recreated.) As of now, the graphics looks amateurish. It needs your professional upgrade. The image of the book has also been uploaded as a file for you to use.

In addition, on the FAQ page, there is a graphic that has been created to fit that area of the page to get the book (circled area of the graphic has been uploaded). I need to have the same graphic you are creating for the home page, but adjust it to be placed on this page. When you recreate the graphic for the FAQ page, there are 2 changes to the text:

1. Change the word "Receive" to "Download." (The rest of the sentence should stay the same.)
2. Delete the entire sentence "Or, pay $17.95 at zellora or tolliver and wrenfield by clicking here.
Nice to have
• Normal file formats such as jpeg, photoshop or ai are fine.

```html
<!DOCTYPE html>
<html lang="en">
<head>
<meta charset="utf-8">
<title>A Gift For You – Free Bride's Guide Opt-in</title>
<link rel="stylesheet" href="https://fonts.googleapis.com/css2?family=Kalam:wght@400;700&family=Montserrat:wght@700&display=swap">
<style>
  :root {
    --teal: #2aa8ab;
    --ink: #1f1f1f;
    --paper: #ffffff;
    --frame: #6b6b6b;
    --cover-light: #f4f1ef;
    --cover-mid: #e6ecec;
    --cover-accent: #bfe3e3;
    --spine: #dcdcdc;
  }
  * { margin: 0; padding: 0; box-sizing: border-box; }
  html, body { width: 1200px; height: 1200px; overflow: hidden; background: var(--paper); }
  .canvas {
    position: relative;
    width: 1200px;
    height: 1200px;
    background: var(--paper);
    border: 1px solid var(--frame);
    overflow: hidden;
  }
  .optin { position: absolute; inset: 0; }
  .optin__title {
    position: absolute;
    width: 640px;
    font-family: "Kalam", cursive;
    font-weight: 700;
    font-size: 92px;
    line-height: 1;
    color: var(--teal);
    white-space: nowrap;
    letter-spacing: -1px;
    text-align: center;
  }
  .optin__rule {
    position: absolute;
    width: 640px;
    height: 3px;
    background: var(--teal);
  }
  .optin__book {
    position: absolute;
    display: block;
  }
  .optin__pitch {
    position: absolute;
    width: 420px;
    font-family: "Kalam", cursive;
    font-weight: 700;
    font-size: 46px;
    line-height: 59px;
    color: var(--ink);
    text-align: center;
    white-space: nowrap;
  }
  .optin__button {
    position: absolute;
    left: 357px;
    top: 404px;
    width: 342px;
    height: 71px;
    border-radius: 36px;
    background: var(--teal);
    color: var(--paper);
    font-family: "Kalam", cursive;
    font-weight: 400;
    font-size: 45px;
    line-height: 75px;
    text-align: center;
    letter-spacing: 2px;
    text-decoration: none;
    white-space: nowrap;
  }
  .optin__download {
    position: absolute;
    left: 749px;
    top: 974px;
    width: 420px;
    font-family: "Montserrat", sans-serif;
    font-weight: 700;
    font-size: 34px;
    line-height: 36px;
    color: var(--teal);
    text-align: center;
    white-space: nowrap;
  }

  .optin--home .optin__title { left: 66px; top: 62px; }
  .optin--home .optin__rule { left: 66px; top: 143px; }
  .optin--home .optin__book { left: 90px; top: 166px; }
  .optin--home .optin__pitch { left: 300px; top: 156px; }

  .optin--faq .optin__title { left: 502px; top: 641px; }
  .optin--faq .optin__rule { left: 502px; top: 722px; }
  .optin--faq .optin__book { left: 526px; top: 746px; }
  .optin--faq .optin__pitch { left: 737px; top: 736px; }
</style>
</head>
<body>
<main class="canvas">

  <section class="optin optin--home">
    <h2 class="optin__title">A Gift For You !</h2>
    <div class="optin__rule"></div>
    <svg class="optin__book" width="260" height="310" viewBox="0 0 260 310" role="img" aria-label="Cover of the free e-book offered to brides">
      <defs>
        <linearGradient id="coverHome" x1="0" y1="0" x2="1" y2="1">
          <stop offset="0" stop-color="var(--cover-light)"/>
          <stop offset="0.6" stop-color="var(--cover-mid)"/>
          <stop offset="1" stop-color="var(--cover-accent)"/>
        </linearGradient>
        <radialGradient id="shadowHome" cx="0.5" cy="0.5" r="0.5">
          <stop offset="0" stop-color="#000" stop-opacity="0.12"/>
          <stop offset="1" stop-color="#000" stop-opacity="0"/>
        </radialGradient>
      </defs>
      <ellipse cx="150" cy="292" rx="110" ry="16" fill="url(#shadowHome)"/>
      <path d="M2 18 L185 2 L186 270 L2 297 Z" fill="url(#coverHome)"/>
      <path d="M2 18 L10 17 L10 296 L2 297 Z" fill="var(--spine)"/>
    </svg>
    <p class="optin__pitch">The ultimate<br>brides guide For<br>buying a wedding<br>cake</p>
    <a class="optin__button" href="http://qvotrl.com/zu-pim/">GET IT NOW</a>
  </section>

  <section class="optin optin--faq">
    <h2 class="optin__title">A Gift For You !</h2>
    <div class="optin__rule"></div>
    <svg class="optin__book" width="260" height="310" viewBox="0 0 260 310" role="img" aria-label="Cover of the free e-book offered to brides">
      <defs>
        <linearGradient id="coverFaq" x1="0" y1="0" x2="1" y2="1">
          <stop offset="0" stop-color="var(--cover-light)"/>
          <stop offset="0.6" stop-color="var(--cover-mid)"/>
          <stop offset="1" stop-color="var(--cover-accent)"/>
        </linearGradient>
        <radialGradient id="shadowFaq" cx="0.5" cy="0.5" r="0.5">
          <stop offset="0" stop-color="#000" stop-opacity="0.12"/>
          <stop offset="1" stop-color="#000" stop-opacity="0"/>
        </radialGradient>
      </defs>
      <ellipse cx="150" cy="292" rx="110" ry="16" fill="url(#shadowFaq)"/>
      <path d="M2 18 L185 2 L186 270 L2 297 Z" fill="url(#coverFaq)"/>
      <path d="M2 18 L10 17 L10 296 L2 297 Z" fill="var(--spine)"/>
    </svg>
    <p class="optin__pitch">The ultimate<br>brides guide For<br>buying a wedding<br>cake</p>
    <p class="optin__download">Download Your Free<br>Copy Now</p>
  </section>

</main>
</body>
</html>
```